Crafted Ember Website

Would like a website designed for my fitness and nutrition coaching company Craft Ember. I have a company logo and would like to keep the page layout clean and simple. Needs to look great on computer and mobile devices.

Target Market(s)

Target market is individuals looking to make changes in their health and nutrition with the help of an online coach.

Industry/Entity Type

Fitness

Number of Pages Required

2 page

Colors
3176b5
0355a3
85acd3
cedeed
f8fcfd
ffffff

Requirements
Must have
• The first page should have the company logo and name towards the top and below that client before and after photos scrolling or displaying in some manner. Also would like a section that states services offered and a section about myself since I am the primary coach for clients.

```html
<!DOCTYPE html>
<html lang="en">
<head>
<meta charset="utf-8">
<title>Crafted Ember</title>
<link rel="stylesheet" href="https://fonts.googleapis.com/css2?family=Montserrat:wght@400;500;600;700&family=Open+Sans:wght@400&display=swap">
<style>
  :root {
    --blue: #1f73ba;
    --blue-deep: #0355a3;
    --blue-soft: #85acd3;
    --ice: #e4edf6;
    --bar: #6d6e71;
    --slate: #58595b;
    --stone: #a7a9ac;
    --text: #6a6b6e;
    --white: #ffffff;
  }
  * { box-sizing: border-box; margin: 0; padding: 0; }
  html, body { width: 788px; height: 1200px; overflow: hidden; background: var(--white); }
  body { position: relative; font-family: "Open Sans", sans-serif; color: var(--text); }
  .block { position: absolute; left: 0; width: 788px; }

  /* top bar */
  .topbar { top: 0; height: 28px; background: var(--bar); }
  .social { position: absolute; left: 16px; top: 10px; display: flex; gap: 6px; }
  .social span { width: 7px; height: 7px; border-radius: 50%; background: var(--white); }
  .main-nav { position: absolute; left: 240px; top: 0; display: flex; height: 28px; }
  .main-nav a { font: 600 7px "Montserrat", sans-serif; letter-spacing: 1.6px; color: var(--white);
    text-decoration: none; line-height: 28px; padding: 0 13px; }
  .main-nav a.active { background: var(--blue); }
  .contact-icons { position: absolute; right: 20px; top: 9px; display: flex; gap: 8px; }

  /* hero */
  .hero { top: 28px; height: 139px; background: linear-gradient(90deg, #2a6fb0, #2f82cb 50%, #3a8bd1); }
  .brand-hero { position: absolute; left: 0; right: 0; top: 60px; display: flex; justify-content: center; align-items: center; gap: 8px; }
  .brand-hero .mark { width: 12px; height: 12px; background: var(--white); }
  .brand-hero .name { font: 600 13px "Montserrat", sans-serif; color: var(--white); letter-spacing: 1px; }

  /* about */
  .about { top: 167px; height: 380px; background: var(--ice); }
  .about-photo { position: absolute; left: 30px; top: 30px; }
  .about-copy { position: absolute; left: 478px; top: 86px; width: 250px; }
  .about-copy h1 { font: 700 27px "Montserrat", sans-serif; color: var(--blue); margin-bottom: 6px; }
  .about-copy p { font-size: 6.6px; line-height: 13.6px; margin-bottom: 6px; padding-left: 4px; }

  /* services */
  .services { top: 547px; height: 255px; }
  .services h2 { position: absolute; top: 36px; width: 100%; text-align: center;
    font: 600 16px "Montserrat", sans-serif; letter-spacing: 7px; color: var(--blue); }
  .service { position: absolute; top: 110px; width: 140px; margin-left: -70px; text-align: center; }
  .service svg.icon { display: block; margin: 0 auto; }
  .service h3 { margin-top: 18px; font: 600 9px "Montserrat", sans-serif; letter-spacing: 3px; color: var(--blue); }
  .more { margin: 16px auto 0; width: 11px; height: 11px; transform: rotate(45deg); background: var(--bar);
    display: flex; align-items: center; justify-content: center; }
  .more span { transform: rotate(-45deg); font: 700 3.5px "Montserrat", sans-serif; color: var(--white); }

  /* transformation band */
  .shape { top: 802px; height: 273px; }
  .shape-copy { position: absolute; left: 0; top: 0; width: 383px; height: 273px; background: var(--stone); }
  .shape-copy .kicker { position: absolute; left: 48px; top: 80px; font: 600 13px "Montserrat", sans-serif; letter-spacing: 5px; color: var(--white); }
  .shape-copy h2 { position: absolute; left: 48px; top: 95px; font: 700 21px "Montserrat", sans-serif; letter-spacing: 7px; color: var(--slate); }
  .shape-copy p { position: absolute; left: 49px; top: 123px; width: 250px; font-size: 6.6px; line-height: 13.6px; color: #3e3f41; }
  .shape-photo { position: absolute; left: 383px; top: 0; width: 405px; height: 273px;
    background: linear-gradient(120deg, #c9c6c0, #8d7a6a 45%, #b9d27a 60%, #d8dcdd); }

  /* footer */
  .footer { top: 1075px; height: 125px; }
  .brand-foot { position: absolute; left: 38px; top: 79px; display: flex; align-items: center; gap: 7px; }
  .brand-foot .mark { width: 12px; height: 12px; background: var(--blue); }
  .brand-foot .name { font: 600 14px "Montserrat", sans-serif; color: var(--blue); }
  .foot-nav { position: absolute; left: 269px; top: 85px; display: flex; gap: 27px; }
  .foot-nav a { font: 600 6.5px "Montserrat", sans-serif; letter-spacing: 1.6px; color: var(--blue); text-decoration: none; }
  .foot-nav a:first-child { color: var(--slate); }
  .foot-icons { position: absolute; left: 680px; top: 84px; display: flex; gap: 6px; align-items: center; }
  .foot-icons .dot { width: 6px; height: 6px; border-radius: 50%; background: var(--bar); }
</style>
</head>
<body>

<header class="block topbar">
  <div class="social"><span></span><span></span><span></span></div>
  <nav class="main-nav">
    <a href="#">HOME</a>
    <a href="#" class="active">ABOUT US</a>
    <a href="#">SERVICES</a>
    <a href="#">GALLERY</a>
    <a href="#">CONTACT US</a>
  </nav>
  <div class="contact-icons">
    <svg width="9" height="9" viewBox="0 0 10 10"><path d="M2 0.5 L3.6 2.6 L2.8 3.6 Q4 6 6.4 7.2 L7.4 6.4 L9.5 8 L8.4 9.5 Q4 9.2 0.5 1.6 Z" fill="#fff"/></svg>
    <svg width="11" height="9" viewBox="0 0 11 8"><rect x="0.5" y="0.5" width="10" height="7" fill="#fff"/><path d="M0.5 0.5 L5.5 4.5 L10.5 0.5" stroke="#6d6e71" stroke-width="0.8" fill="none"/></svg>
  </div>
</header>

<section class="block hero" role="img" aria-label="Blue-tinted gym photo of athletes training">
  <div class="brand-hero"><span class="mark"></span><span class="name">CRAFTED EMBER</span></div>
</section>

<section class="block about">
  <svg class="about-photo" width="450" height="320" viewBox="0 0 450 320" role="img" aria-label="Athlete flipping a large tractor tyre inside a diamond frame">
    <defs>
      <linearGradient id="gymTone" x1="0" y1="0" x2="1" y2="1">
        <stop offset="0" stop-color="#b9bcc0"/>
        <stop offset="0.5" stop-color="#6e6f71"/>
        <stop offset="1" stop-color="#3a3a3a"/>
      </linearGradient>
    </defs>
    <polygon points="226,37 378,189 226,341 74,189" fill="url(#gymTone)" transform="translate(0,-30)"/>
    <polygon points="226,33 382,189 226,345 70,189" fill="none" stroke="#5a5b5e" stroke-width="2.5" transform="translate(0,-30)"/>
    <ellipse cx="200" cy="296" rx="190" ry="4" fill="#000" opacity="0.12"/>
  </svg>
  <div class="about-copy">
    <h1>ABOUT US</h1>
    <p>Net dolorep erepers piciam lignitia pel et eos es explabore se­quaspel mod ut ut ut quis et dus inimporem. Nem dellores estotam exerum faccusa pienim nem rae veratur? Quis et est et eostibus, int ommodis ra corepe dolorporibus aut repudaestium ini volum quiam, cus restistia dolor mi, simeturia volectus.</p>
    <p>Net dolorep erepers piciam lignitia pel et eos es explabore se­quaspel mod ut ut ut quis et dus inimporem. Nem dellores estotam exerum faccusa pienim nem rae veratur? Quis et est et eostibus, int ommodis ra corepe dolorporibus aut repudaestium ini volum quiam, cus restistia dolor mi, simeturia volectus.</p>
  </div>
</section>

<section class="block services">
  <h2>SERVICES</h2>

  <div class="service" style="left:157px">
    <svg class="icon" width="28" height="26" viewBox="0 0 28 26"><circle cx="10" cy="4" r="3.5" fill="#1f73ba"/><rect x="2" y="11" width="22" height="4" rx="2" fill="#1f73ba"/><rect x="2" y="9" width="3" height="10" fill="#1f73ba"/><rect x="22" y="15" width="3" height="9" fill="#1f73ba"/><rect x="6" y="17" width="18" height="2" fill="#1f73ba"/></svg>
    <h3>WEIGHT LIFTING</h3>
    <div class="more"><span>RM</span></div>
  </div>

  <div class="service" style="left:295px">
    <svg class="icon" width="26" height="24" viewBox="0 0 26 24"><path d="M13 22 L2.5 11.5 A6 6 0 0 1 13 4 A6 6 0 0 1 23.5 11.5 Z" fill="#1f73ba"/><path d="M4 12 H9 L11 8 L13 16 L15 11 H22" stroke="#fff" stroke-width="1.3" fill="none"/></svg>
    <h3>CARDIO</h3>
    <div class="more"><span>RM</span></div>
  </div>

  <div class="service" style="left:406px">
    <svg class="icon" width="24" height="28" viewBox="0 0 24 28"><path d="M7 10 V5 A5 5 0 0 1 17 5 V10" stroke="#1f73ba" stroke-width="3" fill="none"/><circle cx="12" cy="17" r="9.5" fill="#1f73ba"/></svg>
    <h3>CROSSFIT</h3>
    <div class="more"><span>RM</span></div>
  </div>

  <div class="service" style="left:528px">
    <svg class="icon" width="24" height="26" viewBox="0 0 24 26"><path d="M12 7 C6 4 2 8 3 14 C4 21 9 25 12 23 C15 25 20 21 21 14 C22 8 18 4 12 7 Z" stroke="#1f73ba" stroke-width="1.6" fill="none"/><path d="M12 7 Q13 3 16 1" stroke="#1f73ba" stroke-width="1.6" fill="none"/><path d="M7 18 L15 10" stroke="#1f73ba" stroke-width="3"/></svg>
    <h3>NUTRITION</h3>
    <div class="more"><span>RM</span></div>
  </div>

  <div class="service" style="left:660px">
    <svg class="icon" width="30" height="24" viewBox="0 0 30 24"><rect x="1" y="9" width="3" height="6" fill="#1f73ba"/><rect x="4" y="3" width="4" height="18" rx="1" fill="#1f73ba"/><rect x="22" y="3" width="4" height="18" rx="1" fill="#1f73ba"/><rect x="26" y="9" width="3" height="6" fill="#1f73ba"/><rect x="8" y="10" width="14" height="4" fill="#1f73ba"/><rect x="10" y="5" width="3" height="14" fill="#1f73ba"/><rect x="17" y="5" width="3" height="14" fill="#1f73ba"/></svg>
    <h3>STRATEGIES</h3>
    <div class="more"><span>RM</span></div>
  </div>
</section>

<section class="block shape">
  <div class="shape-copy">
    <div class="kicker">BEFORE-AFTER</div>
    <h2>SHAPE BODY</h2>
    <p>Net dolorep erepers piciam lignitia pel et eos es explabore se­quaspel mod ut ut ut quis et dus inimporem. Nem dellores estotam exerum faccusa pienim nem rae veratur? Quis et est et eostibus, int ommodis ra corepe dolorporibus aut repudaestium ini volum quiam, cus restistia dolor mi, simeturia volectus.</p>
  </div>
  <div class="shape-photo" role="img" aria-label="Woman in a green sports top measuring her waist with a tape measure"></div>
</section>

<footer class="block footer">
  <div class="brand-foot"><span class="mark"></span><span class="name">CRAFTED EMBER</span></div>
  <nav class="foot-nav">
    <a href="#">HOME</a>
    <a href="#">ABOUT US</a>
    <a href="#">SERVICES</a>
    <a href="#">GALLERY</a>
    <a href="#">CONTACT US</a>
  </nav>
  <div class="foot-icons">
    <svg width="8" height="8" viewBox="0 0 10 10"><path d="M2 0.5 L3.6 2.6 L2.8 3.6 Q4 6 6.4 7.2 L7.4 6.4 L9.5 8 L8.4 9.5 Q4 9.2 0.5 1.6 Z" fill="#6d6e71"/></svg>
    <svg width="10" height="8" viewBox="0 0 11 8"><rect x="0.5" y="0.5" width="10" height="7" fill="#6d6e71"/><path d="M0.5 0.5 L5.5 4.5 L10.5 0.5" stroke="#fff" stroke-width="0.8" fill="none"/></svg>
    <span style="width:18px"></span>
    <span class="dot"></span><span class="dot"></span><span class="dot"></span>
  </div>
</footer>

</body>
</html>
```